Web Design for Small Healthcare Startup

Hello,

We are seeking a Website Design for a healthcare company focusing on mobile vaccinations, employee health and wellness services onsite at businesses, and consulting services relating to Healthcare Entities in WA state. Our company’s mission is to “To aid in a healthier workplace”. Brightpath Rovers will provide on-site wellness services to employers that simplify and streamline employee preventative health as well as onsite consulting services to help with compliance of Healthcare Entities.

We are seeking a Website Design for Brightpath Rovers, PLLC. Our company’s mission is to provide mobile health and wellness services to employers onsite at their businesses. These services include mobile vaccinations clinics for employees as well as wellness and health screenings. The company will also offer healtcare compliance consulting services for Healthcare Entities. The company was founded to bring these important healthcare services to businesses and keep employees healthy. Healthy employees are the cornerstone to a great business and we want to help orginazations achieve their goals of having a healthy productive workforce.

We are looking for a moderin website design that will need to be coded. We have attached our current logo design for reference as well as a brief questionare regarding our business for your information (not necessary to include all information). We would like something SEO friendly and easy to navigate.

Thank you!

Brightpath Rovers, PLLC

Target Market(s)

Small Businesses

Industry/Entity Type

Healthcare

Coding

Coded - Design and coding required

Number of Pages Required

1 page

Requirements
Nice to have
• SEO Friendly, Incorporate Logo

```html
<!DOCTYPE html>
<html lang="en">
<head>
<meta charset="utf-8">
<title>Brightpath Rovers, PLLC – Mobile Vaccine Clinics</title>
<link href="https://fonts.googleapis.com/css2?family=Lato:wght@400;700;900&display=swap" rel="stylesheet">
<style>
:root{
  --purple:#a2459b;
  --blue:#1c5aa6;
  --blue-dark:#164a8c;
  --ink:#2a2a2a;
  --muted:#444;
  --soft:#eef1f7;
  --footer:#2b2f38;
  --white:#fff;
}
*{box-sizing:border-box;margin:0;padding:0}
html,body{width:1200px;height:3874px;overflow:hidden}
body{font-family:'Lato',sans-serif;color:var(--ink);background:var(--white)}
.wrap{width:978px;margin:0 auto;position:relative}
.btn{display:inline-block;background:var(--purple);color:#fff;text-decoration:none;font-weight:700;font-size:19px;border-radius:34px;padding:0 40px;height:68px;line-height:68px;text-transform:uppercase}

.site-header{height:114px}
.site-header .wrap{height:114px}
.brand{position:absolute;left:0;top:30px;display:flex;align-items:center;gap:10px;font-weight:900;font-size:26px;color:var(--blue)}
.brand-dot{width:22px;height:22px;border-radius:50%;background:var(--purple)}
.topbar{position:absolute;right:0;top:22px;font-size:17px;color:var(--ink);display:flex;gap:12px;align-items:center}
.topbar svg{fill:var(--purple);width:14px;height:14px;vertical-align:-2px;margin-right:6px}
.nav{position:absolute;right:0;top:70px;display:flex;gap:25px;font-size:19px}
.nav a{color:var(--ink);text-decoration:none}
.nav a.active{color:var(--purple)}

.hero{height:642px;position:relative;background:linear-gradient(100deg,#5f5c55 0%,#8a7f6e 40%,#c6a367 60%,#b9b4ab 80%,#d8d4cd 100%)}
.hero-copy{position:absolute;left:111px;top:262px;color:#fff}
.hero-copy .kicker{font-size:36px;font-weight:700}
.hero-copy h1{font-size:72px;font-weight:900;margin:10px 0 24px}

.intro{height:247px;text-align:center;padding-top:50px}
.intro h2{font-size:43px;font-weight:700;margin-bottom:24px}
.intro p{font-size:18px;line-height:32px;color:var(--muted)}

.services{height:839px;background:var(--soft);text-align:center;padding-top:52px}
.services h2{font-size:43px;font-weight:700;margin-bottom:38px}
.card-row{display:flex;justify-content:center;gap:30px;margin-bottom:28px}
.card{width:306px;height:283px;border-radius:10px;position:relative;overflow:hidden}
.card span{position:absolute;left:0;right:0;bottom:22px;color:#fff;font-size:22px;font-weight:700}
.c1{background:linear-gradient(180deg,#c9b9a6 0%,#8a86a6 60%,#2d5ea8 100%)}
.c2{background:linear-gradient(180deg,#5a6b7a 0%,#b089a8 60%,#a2459b 100%)}
.c3{background:linear-gradient(180deg,#dfe3e8 0%,#88a7cf 60%,#2563b0 100%)}
.c4{background:linear-gradient(180deg,#d8cdb8 0%,#8a7f9a 60%,#2858a3 100%)}
.c5{background:linear-gradient(180deg,#c7d2dc 0%,#6f86a8 60%,#2858a3 100%)}

.why{height:626px;position:relative}
.why-photo{position:absolute;left:0;top:0;width:654px;height:626px;border-top-right-radius:120px;background:linear-gradient(120deg,#8a8f93 0%,#c66a3a 45%,#a9b0b6 70%,#dcdcdc 100%)}
.why-box{position:absolute;left:567px;top:80px;width:584px;height:472px;background:#fff;box-shadow:0 4px 20px rgba(0,0,0,.12);padding:30px 30px 0 46px}
.why-box h2{font-size:42px;font-weight:700;margin-bottom:24px}
.why-box li{list-style:none;position:relative;padding-left:24px;font-size:16px;line-height:25px;color:var(--muted);margin-bottom:24px}
.why-box li svg{position:absolute;left:0;top:5px;width:15px;height:15px}

.cta{height:308px;background:linear-gradient(90deg,var(--blue-dark),#2466b5,var(--blue-dark));text-align:center;padding-top:74px}
.cta h2{color:#fff;font-size:43px;font-weight:900;margin-bottom:30px}

.schedule{height:707px;text-align:center;padding-top:60px}
.schedule h2{font-size:43px;font-weight:700;margin-bottom:30px}
.steps{display:flex;justify-content:space-between;width:880px;margin:0 auto}
.step{width:290px}
.step-icon{width:162px;height:162px;border-radius:50%;background:var(--soft);margin:0 auto 30px;display:flex;align-items:center;justify-content:center}
.step-icon svg{width:60px;height:60px;fill:var(--purple)}
.step h3{color:var(--blue);font-size:22px;font-weight:400;margin-bottom:16px}
.step p{font-size:19px;line-height:30px;font-weight:700;color:#333}
.call{font-size:24px;margin:60px 0 28px;color:#333}
.call a{color:var(--blue);text-decoration:none}

.site-footer{height:391px;background:var(--footer);color:#fff}
.site-footer .wrap{height:391px}
.footer-brand{position:absolute;left:0;top:110px;display:flex;align-items:center;gap:14px;font-size:40px;font-weight:900;color:#fff}
.footer-brand .brand-dot{width:30px;height:30px}
.links{position:absolute;left:438px;top:60px}
.contact{position:absolute;left:670px;top:60px}
.site-footer h4{font-size:20px;font-weight:700;margin-bottom:20px}
.links a{display:block;color:#fff;text-decoration:none;font-size:16px;line-height:26px}
.contact p{font-size:16px;margin-bottom:30px}
.contact svg{fill:var(--purple);width:13px;height:13px;margin-right:8px;vertical-align:-1px}
.rule{position:absolute;left:0;right:0;top:293px;border-top:1px solid #555b66}
.copy{position:absolute;left:0;top:337px;font-size:16px}
.social{position:absolute;right:0;top:324px;display:flex;gap:8px}
.social span{width:44px;height:44px;border-radius:50%;border:1px solid #7a808b}
</style>
</head>
<body>

<header class="site-header">
  <div class="wrap">
    <div class="brand"><span class="brand-dot"></span>Brightpath Rovers</div>
    <div class="topbar">
      <span><svg viewBox="0 0 16 16"><path d="M3 1l3 3-2 2c1 2 3 4 5 5l2-2 3 3-2 3C6 15 1 10 1 3z"/></svg>509-555-0187</span>
      <span>|</span>
      <span><svg viewBox="0 0 16 16"><path d="M1 3h14v10H1zM1 3l7 6 7-6"/></svg>hello@brightpathrovers.com</span>
    </div>
    <nav class="nav">
      <a class="active" href="#">Home</a><a href="#">About</a><a href="#">Services</a><a href="#">Schedule Today</a><a href="#">Pricing</a><a href="#">Contact</a>
    </nav>
  </div>
</header>

<section class="hero" role="img" aria-label="Photo of a nurse vaccinating a construction worker in a hard hat and safety vest">
  <div class="hero-copy">
    <div class="kicker">Making the workplace a</div>
    <h1>Healthier Place</h1>
    <a class="btn" href="#">Visit Site</a>
  </div>
</section>

<section class="intro">
  <h2>To aid in a healthier workplace</h2>
  <p>Brightpath Rovers specializes in providing seamless, hassle-free, on-site mobile<br>vaccine clinics. No crowded waiting rooms, no long lines, no hassle!</p>
</section>

<section class="services">
  <h2>Services we offer</h2>
  <div class="card-row">
    <div class="card c1" role="img" aria-label="Photo of a woman with a cold"><span>Flu</span></div>
    <div class="card c2" role="img" aria-label="Photo of a woman receiving a vaccine"><span>Covid Booster</span></div>
    <div class="card c3" role="img" aria-label="Photo of an older man receiving a vaccine"><span>Pneumonia Vaccines</span></div>
  </div>
  <div class="card-row">
    <div class="card c4" role="img" aria-label="Photo of a blood pressure check"><span>Wellness Screenings</span></div>
    <div class="card c5" role="img" aria-label="Photo of two doctors in conversation"><span>Consulting Services</span></div>
  </div>
</section>

<section class="why">
  <div class="why-photo" role="img" aria-label="Photo of a nurse checking a construction worker's blood pressure on site"></div>
  <div class="why-box">
    <h2>Why Choose Us</h2>
    <ul>
      <li><svg viewBox="0 0 16 16"><circle cx="8" cy="8" r="8" fill="#1c5aa6"/><path d="M4.5 8.2l2.3 2.3 4.7-4.9" stroke="#fff" stroke-width="2" fill="none"/></svg>Mobile, traveling clinic comes to you to provide vaccines on-site.</li>
      <li><svg viewBox="0 0 16 16"><circle cx="8" cy="8" r="8" fill="#1c5aa6"/><path d="M4.5 8.2l2.3 2.3 4.7-4.9" stroke="#fff" stroke-width="2" fill="none"/></svg>Hassle-free, seamless, avoid congested waiting rooms at<br>medical offices and long lines at local pharmacies.</li>
      <li><svg viewBox="0 0 16 16"><circle cx="8" cy="8" r="8" fill="#1c5aa6"/><path d="M4.5 8.2l2.3 2.3 4.7-4.9" stroke="#fff" stroke-width="2" fill="none"/></svg>Increasing likelihood employees will get vaccinated, reducing<br>workplace illness, sick days, etc.</li>
      <li><svg viewBox="0 0 16 16"><circle cx="8" cy="8" r="8" fill="#1c5aa6"/><path d="M4.5 8.2l2.3 2.3 4.7-4.9" stroke="#fff" stroke-width="2" fill="none"/></svg>Local, Pharmacist owned and operated.</li>
      <li><svg viewBox="0 0 16 16"><circle cx="8" cy="8" r="8" fill="#1c5aa6"/><path d="M4.5 8.2l2.3 2.3 4.7-4.9" stroke="#fff" stroke-width="2" fill="none"/></svg>Cost Transparency, available flexible hours, accommodating<br>to your business needs, employees, spouses, children = less<br>sick days.</li>
    </ul>
  </div>
</section>

<section class="cta">
  <h2>Reserve your on-site mobile vaccine clinic today!</h2>
  <a class="btn" href="#">Book Now</a>
</section>

<section class="schedule">
  <h2>Schedule Today</h2>
  <div class="steps">
    <div class="step">
      <div class="step-icon"><svg viewBox="0 0 24 24"><path d="M12 2l6 6h-4v6h-4V8H6zM2 16h20v6H2zM17 18h2v2h-2z"/></svg></div>
      <h3>Step 1</h3>
      <p>Submit Vaccine Clinic Needs Questionnaire</p>
    </div>
    <div class="step">
      <div class="step-icon"><svg viewBox="0 0 24 24"><path d="M6 1h2v3H6zM16 1h2v3h-2zM2 3h20v20H2zM4 8v13h16V8zM6 10h3v3H6zM10.5 10h3v3h-3zM15 10h3v3h-3zM6 15h3v3H6zM10.5 15h3v3h-3zM15 15h3v3h-3z"/></svg></div>
      <h3>Step 2</h3>
      <p>Brightpath Rovers, PLLC will contact you to schedule on-site vaccine clinic.</p>
    </div>
    <div class="step">
      <div class="step-icon"><svg viewBox="0 0 24 24"><circle cx="12" cy="7" r="4"/><circle cx="4.5" cy="9" r="3"/><circle cx="19.5" cy="9" r="3"/><path d="M5 21c0-5 3-8 7-8s7 3 7 8zM0 19c0-4 2-6 4.5-6 1 0 1.5.2 2 .5C5 15 4.5 17 4.5 19zM24 19c0-4-2-6-4.5-6-1 0-1.5.2-2 .5 1.5 1.5 2 3.5 2 5.5z"/></svg></div>
      <h3>Step 3</h3>
      <p>Prepare your employees for vaccine clinic day.</p>
    </div>
  </div>
  <p class="call">Or call directly for more information <a href="#">(509-555-0187)</a></p>
  <a class="btn" href="#">Visit Site</a>
</section>

<footer class="site-footer">
  <div class="wrap">
    <div class="footer-brand"><span class="brand-dot"></span>Brightpath Rovers</div>
    <div class="links">
      <h4>Quick Links</h4>
      <a href="#">Home</a><a href="#">About</a><a href="#">Services</a><a href="#">Schedule Today</a><a href="#">Pricing</a><a href="#">Contact</a>
    </div>
    <div class="contact">
      <h4>Contact Us</h4>
      <p><svg viewBox="0 0 16 16"><path d="M3 1l3 3-2 2c1 2 3 4 5 5l2-2 3 3-2 3C6 15 1 10 1 3z"/></svg>509-555-0187</p>
      <p><svg viewBox="0 0 16 16"><path d="M1 3h14v10H1z"/></svg>hello@brightpathrovers.com</p>
    </div>
    <div class="rule"></div>
    <div class="copy">© Brightpath Rovers, PLLC. All rights reserved.</div>
    <div class="social"><span></span><span></span><span></span></div>
  </div>
</footer>

</body>
</html>
```